need a clean, modern job advertisement designed for social media (Facebook & Instagram).

The post is to advertise two positions:
• Leading Hand Boilermaker
• Dragline Fitter
We want the design to match our KRT Plant Services branding: blue, white, strong, professional, mining-industry style.
What the design should include:
Bold headline: “WE’RE HIRING”
Sub-headline: “Leading Hand Boilermaker & Dragline Fitter”
Key points:
• Bowen Basin based
• Dragline & shovel maintenance
• Great pay + long-term work
• Locally owned & operated
KRT logo placed cleanly
Space for 1–2 images (boilermaking or dragline work)
Design style:
Strong and industrial
Blue/white colour scheme
Easy to read at a glance
Suitable for a square 1080×1080 design

```html
<!DOCTYPE html>
<html lang="en">
<head>
<meta charset="utf-8">
<title>KRT Plant Services – We're Hiring</title>
<link rel="stylesheet" href="https://fonts.googleapis.com/css2?family=Montserrat:wght@800;900&family=Roboto+Condensed:wght@700&family=Roboto:wght@400;500&display=swap">
<style>
  :root {
    --blue-bright: #1c9ad8;
    --blue-mid: #1e6fb4;
    --blue-deep: #1a3f7a;
    --ink: #262626;
    --white: #ffffff;
    --photo-dark: #14161c;
    --photo-navy: #2a3550;
  }
  * { margin: 0; padding: 0; box-sizing: border-box; }
  html, body {
    width: 1200px; height: 1200px; overflow: hidden; background: var(--white);
  }
  .canvas {
    position: relative;
    width: 1080px; height: 1080px;
    transform: scale(1.111111);
    transform-origin: 0 0;
    background: var(--white);
    overflow: hidden;
  }

  /* Top banner */
  .top-banner {
    position: absolute; left: 0; top: 0; width: 1080px; height: 150px;
  }
  .headline-small {
    position: absolute; left: 92px; top: 32px;
    font-family: "Montserrat", sans-serif; font-weight: 900;
    font-size: 96px; line-height: 1; color: var(--white);
    letter-spacing: 1px;
  }
  .headline-big {
    position: absolute; left: 72px; top: 112px;
    white-space: nowrap;
    font-family: "Montserrat", sans-serif; font-weight: 900;
    font-size: 282px; line-height: 1; color: var(--ink);
    letter-spacing: -2px;
    transform: scaleX(0.86);
    transform-origin: 0 0;
  }
  .headline-big .accent { color: var(--blue-mid); }

  /* Role titles */
  .roles {
    position: absolute; left: 30px; top: 390px; width: 306px;
    font-family: "Roboto Condensed", sans-serif; font-weight: 700;
    font-size: 44px; line-height: 1.25; color: var(--ink);
    text-align: right; text-transform: uppercase;
  }
  .roles .divider {
    height: 4px; background: var(--blue-bright);
    margin: 12px 0 14px 26px;
  }

  /* Photo area */
  .photo {
    position: absolute; left: 375px; top: 393px; width: 643px; height: 322px;
    background:
      radial-gradient(ellipse 260px 180px at 36% 88%, rgba(242,162,60,0.85), rgba(242,162,60,0) 70%),
      radial-gradient(ellipse 320px 260px at 80% 30%, var(--photo-navy), rgba(42,53,80,0) 75%),
      var(--photo-dark);
  }

  /* Logo arc */
  .logo-arc {
    position: absolute; left: 0; top: 0; width: 1080px; height: 1080px;
  }
  .brand {
    position: absolute; left: 70px; top: 840px; width: 400px;
    display: flex; align-items: center; justify-content: center; gap: 12px;
    font-family: "Roboto Condensed", sans-serif; font-weight: 700;
    font-size: 38px; color: var(--blue-deep); white-space: nowrap;
  }
  .brand .dot {
    width: 26px; height: 26px; border-radius: 50%; background: var(--blue-bright);
  }

  /* Key points */
  .points {
    position: absolute; left: 512px; top: 744px; list-style: none;
    font-family: "Roboto Condensed", sans-serif; font-weight: 700;
    font-size: 26px; line-height: 33px; color: var(--ink);
  }
  .points li { position: relative; padding-left: 44px; }
  .points li::before {
    content: "•"; position: absolute; left: 0; top: 0;
  }
  .points li:nth-child(2) { margin-left: 20px; }
  .points li:nth-child(3) { margin-left: 30px; }
  .points li:nth-child(4) { margin-left: 30px; }

  /* Contact */
  .contact {
    position: absolute; left: 545px; top: 898px;
    display: flex; align-items: baseline; gap: 22px; white-space: nowrap;
  }
  .contact .label {
    font-family: "Roboto", sans-serif; font-weight: 400;
    font-size: 48px; color: var(--blue-bright);
  }
  .contact .phone {
    font-family: "Roboto Condensed", sans-serif; font-weight: 700;
    font-size: 56px; color: var(--ink);
  }

  /* Bottom banner */
  .bottom-banner {
    position: absolute; left: 0; top: 960px; width: 1080px; height: 120px;
  }
  .website {
    position: absolute; right: 62px; top: 988px;
    font-family: "Roboto", sans-serif; font-weight: 500;
    font-size: 46px; color: var(--white); letter-spacing: -0.5px;
  }
</style>
</head>
<body>
<main class="canvas">

  <svg class="top-banner" viewBox="0 0 1080 150" aria-hidden="true">
    <defs>
      <linearGradient id="topGrad" x1="0" y1="0" x2="1" y2="0">
        <stop offset="0" stop-color="#1c9ad8"/>
        <stop offset="0.55" stop-color="#1e7cc0"/>
        <stop offset="1" stop-color="#1a3f7a"/>
      </linearGradient>
    </defs>
    <polygon points="28,22 1052,22 1052,138 46,138" fill="url(#topGrad)"/>
    <polygon points="620,138 900,22 1052,22 1052,40 720,138" fill="#ffffff" opacity="0.12"/>
    <polygon points="760,138 1000,40 1052,40 1052,60 860,138" fill="#0e2c5c" opacity="0.25"/>
  </svg>
  <div class="headline-small">WE’RE</div>
  <h1 class="headline-big">HIR<span class="accent">I</span>NG</h1>

  <div class="roles">
    <div>Leading Hand<br>Boilermaker</div>
    <div class="divider"></div>
    <div>Dragline<br>Fitter</div>
  </div>

  <div class="photo" role="img" aria-label="Photo of a welder in a helmet and gloves welding steel, with sparks flying"></div>

  <svg class="logo-arc" viewBox="0 0 1080 1080" aria-hidden="true">
    <path d="M55,880 A215,215 0 0 1 485,880 L485,960 L55,960 Z" fill="#ffffff"/>
    <path d="M55,880 A215,215 0 0 1 485,880" fill="none" stroke="#1c9ad8" stroke-width="5"/>
  </svg>
  <div class="brand"><span class="dot"></span><span>KRT Plant Services</span></div>

  <ul class="points">
    <li>Bowen Basin based</li>
    <li>Dragline &amp; shovel maintenance</li>
    <li>Great pay + long-term work</li>
    <li>Locally owned &amp; operated</li>
  </ul>

  <div class="contact">
    <span class="label">Contact</span>
    <span class="phone">0400 555 182</span>
  </div>

  <svg class="bottom-banner" viewBox="0 960 1080 120" aria-hidden="true">
    <defs>
      <linearGradient id="botGrad" x1="0" y1="0" x2="1" y2="0">
        <stop offset="0" stop-color="#1c9ad8"/>
        <stop offset="0.5" stop-color="#1e7cc0"/>
        <stop offset="1" stop-color="#1a3f7a"/>
      </linearGradient>
    </defs>
    <polygon points="14,972 1066,972 1066,1058 14,1058" fill="url(#botGrad)"/>
    <polygon points="14,972 440,972 380,1058 14,1058" fill="#1c9ad8"/>
  </svg>
  <div class="website">www.krtplantservices.com</div>

</main>
</body>
</html>
```